Private Investigation Business Card Design

I need a business card for a new private investigation company named Brisk Lens Inquiries. I perform mainly surveillance jobs, vehicle repossessions, document serves etc. The final design should aim for a professional look. The logo has a magnifying glass with stick man arms and legs and is in a running action to show the "BRISK" aspect of the name. If the colour scheme could remain the same as the website www.brisklensinquiries.example.au with silvers,blacks and a couple electric blue highlights.
Industry/Entity Type
Business
Contact Information for Business Card
Morgan Kilbride
Brisk Lens Inquiries
0438276104
PO Box 58, Fernvale NSW 2291
info@brisklensinquiries.example.au
www.brisklensinquiries.example.au
Look and feel
Each slider illustrates characteristics of the customer's brand and the style your logo design should communicate.

```html
<!DOCTYPE html>
<html lang="en">
<head>
<meta charset="utf-8">
<title>Brisk Lens Inquiries — Business Card</title>
<link rel="stylesheet" href="https://fonts.googleapis.com/css2?family=Archivo+Black&family=Jura:wght@500&family=Michroma&display=swap">
<style>
  :root {
    --backdrop: #efeae2;
    --card-white: #ffffff;
    --ink-black: #231f20;
    --electric-blue: #4a9ed8;
    --steel: #4d4d50;
    --silver: #d9d9dc;
    --icon-grey: #6d6d70;
    --social-1: #3b5998;
    --social-2: #2ba3e0;
    --social-3: #1c6ea4;
    --social-4: #d7312b;
  }
  * { box-sizing: border-box; margin: 0; padding: 0; }
  html, body {
    width: 1189px; height: 1200px; overflow: hidden;
    background: var(--backdrop);
  }
  .card {
    position: absolute; left: 204px; width: 792px; height: 488px;
    background: var(--card-white); overflow: hidden;
    box-shadow: 0 2px 6px rgba(0,0,0,0.18);
  }
  .card--front { top: 67px; }
  .card--back { top: 627px; }
  .card__bands { position: absolute; inset: 0; width: 792px; height: 488px; }
  .wordmark {
    position: absolute; color: var(--steel);
    font-family: "Michroma", sans-serif; font-weight: 400;
    line-height: 1; white-space: nowrap;
  }
  .wordmark__main { display: block; letter-spacing: 2px; }
  .wordmark__sub { display: block; }
  .card--front .wordmark { left: 92px; top: 182px; }
  .card--front .wordmark__main { font-size: 96px; }
  .card--front .wordmark__sub { font-size: 31px; letter-spacing: 9px; margin-top: 14px; }
  .card--back .wordmark { left: 51px; top: 62px; }
  .card--back .wordmark__main { font-size: 82px; }
  .card--back .wordmark__sub { font-size: 27px; letter-spacing: 7px; margin-top: 10px; }
  .mark-dot {
    position: absolute; border-radius: 50%;
    background: radial-gradient(circle at 40% 40%, #f4f4f5, var(--silver));
  }
  .card--front .mark-dot { left: 600px; top: 188px; width: 74px; height: 74px; }
  .card--back .mark-dot { left: 545px; top: 150px; width: 120px; height: 120px; }
  .card__name {
    position: absolute; left: 51px; top: 204px;
    font-family: "Archivo Black", sans-serif; font-size: 35px;
    color: var(--ink-black); letter-spacing: 1px; white-space: nowrap;
  }
  .contact-list { position: absolute; left: 51px; top: 264px; list-style: none; }
  .contact-list__item {
    display: flex; align-items: center; height: 29px;
    font-family: "Jura", sans-serif; font-weight: 500; font-size: 23px;
    color: var(--ink-black); white-space: nowrap;
  }
  .contact-list__icon { width: 22px; height: 22px; margin-right: 12px; flex: none; }
  .social-row { position: absolute; left: 570px; top: 67px; display: flex; gap: 18px; }
  .social-row__tile { width: 31px; height: 31px; border-radius: 2px; }
  .social-row__tile--a { background: var(--social-1); }
  .social-row__tile--b { background: var(--social-2); }
  .social-row__tile--c { background: var(--social-3); }
  .social-row__tile--d { background: var(--social-4); }
  .card__address {
    position: absolute; right: 49px; top: 412px; text-align: right;
    font-family: "Jura", sans-serif; font-weight: 500; font-size: 23px;
    line-height: 26px; color: var(--card-white); white-space: nowrap;
  }
</style>
</head>
<body>

<section class="card card--front">
  <svg class="card__bands" viewBox="0 0 792 488" aria-hidden="true">
    <path d="M0 0H792V54C560 100 300 113 0 110Z" fill="var(--ink-black)"/>
    <path d="M90 121C350 126 600 100 792 66V117C600 132 320 132 90 121Z" fill="var(--electric-blue)"/>
    <path d="M0 370C220 350 500 352 698 366C450 364 220 384 0 420Z" fill="var(--electric-blue)"/>
    <path d="M0 433C250 388 500 372 792 374V488H0Z" fill="var(--ink-black)"/>
  </svg>
  <div class="wordmark">
    <span class="wordmark__main">BRISK</span>
    <span class="wordmark__sub">LENS INQUIRIES</span>
  </div>
  <div class="mark-dot" aria-hidden="true"></div>
</section>

<section class="card card--back">
  <svg class="card__bands" viewBox="0 0 792 488" aria-hidden="true">
    <path d="M0 373C220 352 500 354 698 367C450 366 220 386 0 422Z" fill="var(--electric-blue)"/>
    <path d="M0 434C250 390 500 375 792 375V488H0Z" fill="var(--ink-black)"/>
  </svg>
  <div class="wordmark">
    <span class="wordmark__main">BRISK</span>
    <span class="wordmark__sub">LENS INQUIRIES</span>
  </div>
  <div class="social-row" aria-hidden="true">
    <span class="social-row__tile social-row__tile--a"></span>
    <span class="social-row__tile social-row__tile--b"></span>
    <span class="social-row__tile social-row__tile--c"></span>
    <span class="social-row__tile social-row__tile--d"></span>
  </div>
  <div class="mark-dot" aria-hidden="true"></div>
  <h1 class="card__name">MORGAN KILBRIDE</h1>
  <ul class="contact-list">
    <li class="contact-list__item">
      <svg class="contact-list__icon" viewBox="0 0 22 22" aria-hidden="true">
        <rect width="22" height="22" fill="var(--icon-grey)"/>
        <path d="M7 4h3l1 4-2 1.5c1 2 2 3 3.5 3.5L14 11l4 1v3c-6 1-12-5-11-11Z" fill="#fff"/>
      </svg>0438276104</li>
    <li class="contact-list__item">
      <svg class="contact-list__icon" viewBox="0 0 22 22" aria-hidden="true">
        <rect width="22" height="22" fill="var(--icon-grey)"/>
        <rect x="4" y="6" width="14" height="10" fill="none" stroke="#fff" stroke-width="1.5"/>
        <path d="M4 6l7 6 7-6" fill="none" stroke="#fff" stroke-width="1.5"/>
      </svg>info@brisklensinquiries.example.au</li>
    <li class="contact-list__item">
      <svg class="contact-list__icon" viewBox="0 0 22 22" aria-hidden="true">
        <rect width="22" height="22" fill="var(--icon-grey)"/>
        <circle cx="11" cy="11" r="7" fill="none" stroke="#fff" stroke-width="1.3"/>
        <ellipse cx="11" cy="11" rx="3" ry="7" fill="none" stroke="#fff" stroke-width="1.2"/>
        <path d="M4 11h14M5.5 7.5h11M5.5 14.5h11" stroke="#fff" stroke-width="1"/>
      </svg>www.brisklensinquiries.example.au</li>
  </ul>
  <p class="card__address">PO Box 58, Fernvale<br>NSW 2291</p>
</section>

</body>
</html>
```